I apologize on the fact that star rating on the same design will change during the contest. But you are making so many design, which is great :) , but make the selection quite difficult... Will do my best to give you information of what I like, but it will take some time...
Will it be possible to upload your creation without putting them like in 3D view. I am not comfortable to do a selection on design with a 60° of view angle ;)
And also if you can just have a neutral background around the card it will be more easy...
Just a small precision... In the Brief I describe that I would like a black or white background to see how it will look.
This white or black color has to be on the card itself as the "background" beside the logo (that's why I have put two logos) and not around the business card.
I have just uploaded a zip file containing all file formats for the logo.
Kind Regards,
Marc Delorme
Kind regards,

```html
<!DOCTYPE html>
<html lang="en">
<head>
<meta charset="utf-8">
<title>Skyward Console – Business Card</title>
<link rel="stylesheet" href="https://fonts.googleapis.com/css2?family=Arimo:wght@400;700&display=swap">
<style>
  :root {
    --backdrop: #d9d9d9;
    --card: #3c3c3e;
    --text-light: #e6e6e6;
    --text-dim: #bdbdbd;
    --blue: #1b8fd8;
    --blue-deep: #0c5fa8;
    --silver-a: #f2f2f2;
    --silver-b: #8d8d8d;
    --orange: #f07a12;
  }
  * { margin: 0; padding: 0; box-sizing: border-box; }
  html, body { width: 1200px; height: 941px; overflow: hidden; }
  body {
    background: var(--backdrop);
    font-family: "Arimo", Arial, sans-serif;
    position: relative;
  }
  .card {
    position: absolute;
    background: var(--card);
    border-radius: 22px;
    overflow: hidden;
  }
  .card--front { left: 46px; top: 51px; width: 734px; height: 427px; }
  .card--back  { left: 419px; top: 488px; width: 717px; height: 414px; }

  .brand {
    position: absolute;
    display: flex;
    align-items: center;
    gap: 14px;
    color: var(--blue);
    font-weight: 700;
    white-space: nowrap;
  }
  .brand__dot {
    border-radius: 50%;
    background: var(--orange);
    flex: none;
  }
  .card--front .brand { left: 76px; top: 100px; font-size: 40px; }
  .card--front .brand__dot { width: 40px; height: 40px; }

  .address {
    position: absolute; left: 76px; top: 262px;
    font-size: 13px; line-height: 19px; color: var(--text-light);
  }
  .rule {
    position: absolute; left: 300px; top: 283px; width: 180px;
    border-top: 1px dashed var(--text-dim);
  }
  .person { position: absolute; right: 53px; top: 258px; text-align: right; }
  .person__name { font-size: 19px; color: var(--blue); }
  .person__role { font-size: 12px; color: var(--text-light); margin-top: 5px; }

  .contact {
    position: absolute; left: 76px; top: 314px;
    font-size: 12px; line-height: 19px; color: var(--text-light);
    list-style: none;
  }
  .contact li { display: flex; align-items: center; gap: 8px; }
  .contact svg { width: 13px; height: 13px; fill: var(--blue); }

  .strip-silver {
    position: absolute; left: 0; top: 380px; width: 370px; height: 30px;
    background: linear-gradient(180deg, var(--silver-a), var(--silver-b));
  }
  .strip-blue {
    position: absolute; left: 390px; top: 380px; right: 0; height: 30px;
    background: linear-gradient(180deg, #3aa9ec, var(--blue-deep));
    border-radius: 15px 0 0 15px;
    color: #fff; font-size: 15px; font-weight: 700;
    display: flex; align-items: center; padding-left: 110px;
  }
  .strip-dot {
    position: absolute; left: 400px; top: 375px; width: 40px; height: 40px;
    border-radius: 50%; background: var(--orange);
  }

  .card--back .brand {
    left: 0; right: 0; top: 130px; justify-content: center; font-size: 52px;
  }
  .card--back .brand__dot { width: 52px; height: 52px; }
  .web {
    position: absolute; left: 0; right: 0; top: 258px; text-align: center;
    font-size: 30px; font-weight: 700; color: var(--blue);
  }
  .web-rule {
    position: absolute; left: 160px; right: 160px; top: 302px; height: 2px;
    background: linear-gradient(90deg, transparent, var(--blue), transparent);
  }
</style>
</head>
<body>
  <section class="card card--front">
    <div class="brand"><span class="brand__dot"></span>Skyward Console</div>

    <p class="address">42, Chemin des Tilleuls<br>1219 Vernier, Switzerland</p>
    <div class="rule"></div>
    <div class="person">
      <p class="person__name">Marc Delorme</p>
      <p class="person__role">Founder | Chief Concept Officer</p>
    </div>

    <ul class="contact">
      <li><svg viewBox="0 0 24 24"><path d="M6.6 10.8a15 15 0 0 0 6.6 6.6l2.2-2.2a1 1 0 0 1 1-.25 11.4 11.4 0 0 0 3.6.57 1 1 0 0 1 1 1V20a1 1 0 0 1-1 1A17 17 0 0 1 3 4a1 1 0 0 1 1-1h3.5a1 1 0 0 1 1 1c0 1.25.2 2.45.57 3.57a1 1 0 0 1-.25 1z"/></svg>+41-22-5550148</li>
      <li><svg viewBox="0 0 24 24"><path d="M2 5h20v14H2zm2 2v.5l8 5 8-5V7l-8 5z"/></svg>marc.delorme@skywardconsole.com</li>
    </ul>

    <div class="strip-silver"></div>
    <div class="strip-blue">www.skywardconsole.com</div>
    <div class="strip-dot"></div>
  </section>

  <section class="card card--back">
    <div class="brand"><span class="brand__dot"></span>Skyward Console</div>
    <p class="web">www.skywardconsole.com</p>
    <div class="web-rule"></div>
  </section>
</body>
</html>
```